psd/html for a e wallet payment website designed

hi
i am in need of a psd / html for a whole website designed
the site is a e wallet /payment system i can i will provide a link to what type of style i am looking for but i can not stress this enough i do not want anyone replicating the website i am just providing the links to show you what kind of function and the content that is involved also, i have a srs with detailed pages you can read and refer to if need be
thanks of viewing
Plimvora.com
Quindrel.com
brankowelt.com
Tazurnik.com

```html
<!DOCTYPE html>
<html lang="en">
<head>
<meta charset="utf-8">
<title>Velsoria – Pay online, safely and easily</title>
<link href="https://fonts.googleapis.com/css2?family=Open+Sans:wght@300;400;600;700&display=swap" rel="stylesheet">
<style>
:root{
  --green:#5cb227;
  --green-dark:#3f8d14;
  --green-text:#54a51f;
  --ink:#2a2a2a;
  --grey:#666;
  --grey-light:#9a9a9a;
  --blue:#1e8fe0;
  --rule:#232323;
  --footer-top:#3b3b3b;
  --footer-bottom:#1f1f1f;
  --base:#181818;
  --white:#fff;
}
*{margin:0;padding:0;box-sizing:border-box}
html,body{width:849px;height:1200px;overflow:hidden;background:var(--white)}
body{font-family:"Open Sans",Arial,sans-serif;color:var(--ink);position:relative}
.abs{position:absolute}

/* header */
.brand{left:138px;top:14px;font-size:44px;font-weight:400;color:var(--green);letter-spacing:-1px;line-height:1}
.btn-mini{top:13px;width:53px;height:17px;border-radius:3px;color:var(--white);font-size:7px;font-weight:700;text-align:center;line-height:17px;text-transform:uppercase}
.btn-signin{left:480px;background:var(--blue)}
.btn-signup{left:540px;background:var(--green)}
.social-sq{top:13px;width:15px;height:15px;border-radius:2px}
.main-nav{left:335px;top:64px;height:29px;display:flex}
.main-nav a{display:block;height:29px;line-height:29px;padding:0 10px;font-size:10.5px;color:#555;text-decoration:none;text-transform:uppercase;border-left:1px solid #ddd}
.main-nav a.active{background:var(--green);color:var(--white);border-left:none;padding:0 12px}

/* hero */
.hero{left:0;top:93px;width:849px;height:284px;background:linear-gradient(90deg,#e9e9e9 0%,#f2f3f2 30%,#dfe6ea 55%,#d6e5c4 80%,#c2da9a 100%)}
.hero-title{left:137px;top:126px;font-size:42px;font-weight:300;line-height:52px;letter-spacing:-1.5px;color:var(--ink)}
.hero-title .hl{color:var(--green)}
.hero-rule{left:137px;width:266px;height:1px;background:#bfd9a8}
.hero-sub{left:137px;top:256px;font-size:16.5px;font-weight:300;color:#333}
.btn-pill{border-radius:12px;background:var(--green);color:var(--white);text-align:center;font-size:11px}
.btn-more{left:136px;top:305px;width:86px;height:23px;line-height:23px}
.hero-media{left:421px;top:134px;width:289px;height:192px;background:linear-gradient(135deg,#d9d9d9,#f4f4f4 50%,#cfcfcf);box-shadow:0 2px 6px rgba(0,0,0,.2)}

/* call to action band */
.band-rule{left:0;width:849px;height:3px;background:var(--rule)}
.cta-text{left:142px;font-size:15.5px;font-weight:400;color:#333}
.cta-text strong{color:var(--green);font-weight:600}
.btn-cta{left:530px;width:150px;height:24px;line-height:24px;font-size:11px;text-transform:uppercase}

/* services */
.services{left:130px;top:439px;width:579px;height:189px;border:1px solid #d6d6d6;background:linear-gradient(#fff 30%,#e6e9df)}
.svc-art{border-radius:4px}
.svc-title{font-size:13px;font-weight:400;color:var(--green-text)}
.svc-text{font-size:8.3px;line-height:14.5px;color:#555;width:160px}

/* features */
.features-title{left:0;width:830px;top:643px;text-align:center;font-size:23px;font-weight:400;color:var(--green)}
.feat-icon{width:26px;height:26px}
.feat-title{font-size:13.5px;font-weight:600;color:var(--green-text)}
.feat-text{font-size:9.5px;line-height:11.5px;color:var(--grey-light);width:175px}

/* footer */
.site-footer{left:0;top:922px;width:849px;height:218px;background:linear-gradient(var(--footer-top),var(--footer-bottom))}
.foot-head{font-size:9.5px;font-weight:700;color:var(--white);text-transform:uppercase}
.foot-list{list-style:none;font-size:7px;line-height:12px;color:#ddd}
.foot-social li{display:flex;align-items:center;gap:6px;line-height:15px}
.foot-social i{display:inline-block;width:8px;height:8px;border-radius:1px}
.footer-accent{left:0;top:1139px;width:849px;height:2px;background:var(--green)}
.footer-base{left:0;top:1141px;width:849px;height:59px;background:var(--base)}
.copyright{left:143px;top:1161px;font-size:7px;font-weight:700;color:var(--white)}
.badge{top:1152px;height:30px;border-radius:3px;background:#f2f2f2}
</style>
</head>
<body>

<header>
  <div class="abs brand">Velsoria</div>
  <a class="abs btn-mini btn-signin">Sign in</a>
  <a class="abs btn-mini btn-signup">Sign up</a>
  <span class="abs social-sq" style="left:630px;background:#3fb5e8"></span>
  <span class="abs social-sq" style="left:651px;background:#3b5b98"></span>
  <span class="abs social-sq" style="left:672px;background:#333"></span>
  <span class="abs social-sq" style="left:693px;background:#f08a1c"></span>
  <nav class="abs main-nav">
    <a class="active">Personal</a>
    <a>Business</a>
    <a>E Wallet / Payment</a>
    <a>Support</a>
    <a>Blog</a>
  </nav>
</header>

<section class="abs hero"></section>
<h1 class="abs hero-title"><span class="hl">pay</span> online,<br>safely<span class="hl">and</span>easily</h1>
<div class="abs hero-rule" style="top:248px"></div>
<p class="abs hero-sub">Optimize for smartphones and tablets</p>
<div class="abs hero-rule" style="top:286px"></div>
<a class="abs btn-pill btn-more">More Info</a>
<div class="abs hero-media" role="img" aria-label="Hand holding a smartphone showing a video play button and the Velsoria name"></div>

<div class="abs band-rule" style="top:377px"></div>
<p class="abs cta-text" style="top:396px">Get Started With Your <strong>FREE E-WALLET</strong> Acount</p>
<a class="abs btn-pill btn-cta" style="top:395px">Get your account</a>

<section class="abs services"></section>
<div class="abs svc-art" style="left:176px;top:444px;width:106px;height:68px;background:radial-gradient(circle,#7bc043 0%,#5a9a2a 60%,#fff 100%)" role="img" aria-label="Globe with people and currency coins illustrating sending money"></div>
<h3 class="abs svc-title" style="left:152px;top:519px">Send Money</h3>
<p class="abs svc-text" style="left:152px;top:544px">Shop or send money online to anyone in over 190 countries safely and easily without sharing your personal information. It's always free!</p>

<div class="abs svc-art" style="left:335px;top:460px;width:160px;height:44px;background:linear-gradient(90deg,#e8e8e8,#d7dde6)" role="img" aria-label="Row of accepted payment method marks"></div>
<h3 class="abs svc-title" style="left:333px;top:519px">Receive Money</h3>
<p class="abs svc-text" style="left:333px;top:544px">Manage payments for your business or sell your products/services online with ease and security. Receive your money instantly!</p>

<div class="abs svc-art" style="left:537px;top:446px;width:126px;height:70px;background:linear-gradient(90deg,#5cb227 55%,#333 56%)" role="img" aria-label="Green prepaid card in front of a dark card"></div>
<h3 class="abs svc-title" style="left:518px;top:522px">Fast Deposits and Withdrawals</h3>
<p class="abs svc-text" style="left:518px;top:544px">Get your money in and out of your E-wallet faster, easier and cheaper! Our flexible deposit and withdrawal options give you the choice!</p>

<h2 class="abs features-title">FEATURES</h2>

<!-- left features -->
<svg class="abs feat-icon" style="left:150px;top:688px" viewBox="0 0 26 26"><circle cx="13" cy="10" r="3" fill="#222"/><path d="M6 16a9 9 0 1 1 14 0M9 13.5a5 5 0 1 1 8 0" fill="none" stroke="#222" stroke-width="2"/><rect x="12" y="12" width="2" height="12" fill="#222"/></svg>
<h3 class="abs feat-title" style="left:193px;top:685px">Instant transactions</h3>
<p class="abs feat-text" style="left:193px;top:704px">Payments to others are instant; there is no waiting for clearing of funds.</p>

<svg class="abs feat-icon" style="left:150px;top:740px" viewBox="0 0 26 26"><rect x="2" y="4" width="22" height="18" rx="3" fill="none" stroke="#222" stroke-width="2"/><path d="M17 10h7v6h-7z" fill="none" stroke="#222" stroke-width="2"/></svg>
<h3 class="abs feat-title" style="left:193px;top:738px">Multiple wallets</h3>
<p class="abs feat-text" style="left:193px;top:757px">Keep better track of your online funds with our wallet system.</p>

<svg class="abs feat-icon" style="left:150px;top:793px" viewBox="0 0 26 26"><rect x="1" y="7" width="24" height="15" rx="2" fill="#222"/><rect x="8" y="4" width="10" height="4" fill="#222"/><circle cx="13" cy="14.5" r="4" fill="#fff"/><circle cx="13" cy="14.5" r="2" fill="#222"/></svg>
<h3 class="abs feat-title" style="left:193px;top:791px">Easy to deposit and withdraw</h3>
<p class="abs feat-text" style="left:193px;top:810px">Simple transfers to and from your e-wallet account, plus other flexible options.</p>

<!-- right features -->
<svg class="abs feat-icon" style="left:464px;top:686px" viewBox="0 0 26 26"><circle cx="13" cy="13" r="12" fill="#222"/><path d="M7 8c3 0 4 3 7 2s2 5-1 5-2 4-4 3-2-5-4-6 0-4 2-4zM17 15c2 0 3 2 2 4s-3 1-3-1 0-3 1-3z" fill="#fff"/></svg>
<h3 class="abs feat-title" style="left:508px;top:681px">Safe online environment</h3>
<p class="abs feat-text" style="left:508px;top:701px">The E-wallet website is built to protect your funds.</p>

<svg class="abs feat-icon" style="left:464px;top:735px" viewBox="0 0 26 26"><circle cx="7" cy="11" r="3.5" fill="#222"/><path d="M1 26v-6a6 6 0 0 1 12 0v6z" fill="#222"/><path d="M13 2h11v8h-6l-3 3v-3h-2z" fill="none" stroke="#222" stroke-width="1.5"/></svg>
<h3 class="abs feat-title" style="left:508px;top:731px">Great customer support</h3>
<p class="abs feat-text" style="left:508px;top:748px">E-wallet offers second to none customer support.</p>

<svg class="abs feat-icon" style="left:464px;top:788px" viewBox="0 0 26 26"><circle cx="11" cy="7" r="5" fill="#222"/><path d="M1 24a10 10 0 0 1 20 0z" fill="#222"/><circle cx="20" cy="12" r="3" fill="#222"/><path d="M15 24a6 6 0 0 1 10 0z" fill="#222"/></svg>
<h3 class="abs feat-title" style="left:508px;top:789px">Residual affiliate income</h3>
<p class="abs feat-text" style="left:508px;top:809px">E-wallet offers a simple yet extremely rewarding affiliate program.</p>

<div class="abs band-rule" style="top:864px"></div>
<p class="abs cta-text" style="top:883px">Get Started With Your <strong>FREE E-WALLET</strong> Acount</p>
<a class="abs btn-pill btn-cta" style="top:882px">Get your account</a>

<footer>
  <div class="abs site-footer"></div>

  <h4 class="abs foot-head" style="left:145px;top:942px">About E-wallet</h4>
  <ul class="abs foot-list" style="left:145px;top:964px">
    <li>Vision and Mission</li><li>About Us</li><li>Careers</li><li>Customer Testimonials</li><li>Merchant Testimonials</li><li>Media</li>
  </ul>
  <h4 class="abs foot-head" style="left:145px;top:1047px">Support</h4>
  <ul class="abs foot-list" style="left:145px;top:1062px">
    <li>FAQs</li><li>Fees</li><li>Featured Merchants</li><li>Contact us</li>
  </ul>

  <h4 class="abs foot-head" style="left:286px;top:942px">Features</h4>
  <ul class="abs foot-list" style="left:286px;top:964px">
    <li>How E-wallet Works</li><li>E-wallet Prepaid Card</li><li>Add Funds and Withdraw</li><li>Pay and Get Paid</li><li>Send Funds</li><li>SimplySendXY</li><li>Business Profiles</li><li>Corporate Disbursements</li><li>Request Funds and Send</li><li>Local Payment Options</li><li>Available Currencies</li><li>Referral Program</li>
  </ul>

  <h4 class="abs foot-head" style="left:433px;top:942px">Legal Agreements</h4>
  <ul class="abs foot-list" style="left:433px;top:964px">
    <li>Terms &amp; Conditions</li><li>Online Privacy Policy</li><li>Infringement Policy</li><li>Formal Complaint</li>
  </ul>
  <h4 class="abs foot-head" style="left:438px;top:1047px">Developers</h4>
  <ul class="abs foot-list" style="left:438px;top:1064px">
    <li>Developer Center</li><li>Sandbox</li><li>Shopping Carts</li>
  </ul>

  <h4 class="abs foot-head" style="left:608px;top:943px">Security</h4>
  <ul class="abs foot-list" style="left:608px;top:966px">
    <li>Security Center</li><li>Fraud Prevention</li><li>Buyer Protection</li><li>Merchant Protection</li>
  </ul>
  <h4 class="abs foot-head" style="left:607px;top:1046px">Follow us</h4>
  <ul class="abs foot-list foot-social" style="left:607px;top:1065px">
    <li><i style="background:#3b5b98"></i>Linkwall</li>
    <li><i style="background:#3fb5e8"></i>Chirpline</li>
    <li><i style="background:#f08a1c"></i>Blog</li>
  </ul>

  <div class="abs footer-accent"></div>
  <div class="abs footer-base"></div>
  <p class="abs copyright">Copyright © 2014 E-wallet. All rights reserved.</p>
  <div class="abs badge" style="left:483px;width:60px;background:#2f6fb0"></div>
  <div class="abs badge" style="left:548px;width:80px"></div>
  <div class="abs badge" style="left:635px;width:78px"></div>
</footer>

</body>
</html>
```